Wholistic Health Clinic (Chiropractic Osteopathic Naturapathic Homeopathic New Website Design

Create a beautiful website for Tallowmere Chiropractic clinic that has been in the Sutherland Shire for over 40 years, that exemplifies the passion for helping people with their health goals using that may include a variety of techniques including Chiropractic, Osteopathy, Acupuncture, Applied Kinesiology, Retained Neonatal Reflexes, Nutritional Advice, Exercise Prescription, Decompression therapy, Massage and Stress management techniques.
We have a wholistic approach that includes Nutritional, Emotional and Physical health

(A more detailed draft will be supplied shortly)

Pages:
Home page
About Us Page
Team Page
Contact page
Terms of service Page
Privacy Page
and any other relevant page(s)

Will supply photos for:
- The Team Page and their qualifications & brief resume
- About Us page

Will supply logos for:
NRB
PLUVEX
VITALOAN
JOBSHIELD
RTQ
KPO

Target Market(s)

main target Parents of young children and those 20's to 60's who live in the Sutherland Shire & have disposable income (that said almost everybody would benefit from their services)

Coding

Coded - Design and coding required

Number of Pages Required

5+ page

Font styles to use
Sans Serif

Requirements
Must have
• Please follow the brief

1. Easy to manage ourselves to add alerts (like Covid 19 compliance & Posture fortnight etc.) & update content like photos of team members etc.
2. Must be responsive and look good on mobile devices
3. must be fast loading
4. Logo on every page
5. Easy navigation on every page
6. Phone number must be clickable
7. Terms of service & Privacy pages
8. Slider on page 1 using photo of healthy people of all ages enjoying various lifestyles & ability to add other photos easily
Should not have
• no testimonials or any non compliant elements according to the NRB

```html
<!DOCTYPE html>
<html lang="en">
<head>
<meta charset="utf-8">
<title>Tallowmere Chiropractic – Wholistic Health Clinic</title>
<link href="https://fonts.googleapis.com/css2?family=Lato:wght@400;700;900&display=swap" rel="stylesheet">
<style>
:root{
  --purple:#3f3650;
  --purple-deep:#352c45;
  --olive:#bcb383;
  --olive-dark:#a79f6d;
  --ink:#333;
  --muted:#666;
  --white:#fff;
  --line:#e6e6e6;
}
*{box-sizing:border-box;margin:0;padding:0}
html,body{width:1200px;height:3822px;overflow:hidden}
body{font-family:'Lato',sans-serif;color:var(--ink);background:var(--white);position:relative}
.abs{position:absolute}
.btn{position:absolute;display:flex;align-items:center;justify-content:center;gap:8px;background:var(--olive);color:var(--white);border-radius:30px;font-weight:700;text-transform:uppercase;white-space:nowrap}
.btn .dot{width:11px;height:11px;border-radius:50%;background:var(--white);position:relative}
.btn .dot::after{content:"";position:absolute;left:4px;top:3px;border-left:4px solid var(--olive);border-top:2.5px solid transparent;border-bottom:2.5px solid transparent}
/* header */
.header{position:absolute;left:0;top:0;width:1200px;height:104px;background:var(--white);border-top:4px solid var(--olive)}
.brand{position:absolute;left:144px;top:30px;display:flex;align-items:center;gap:10px}
.brand .mark{width:44px;height:44px;border-radius:50%;background:var(--purple)}
.brand .name{font-size:17px;font-weight:700;color:#222;line-height:1.1}
.brand .name small{display:block;font-size:9px;font-weight:900;letter-spacing:.2px}
.callbar{position:absolute;left:480px;top:12px;display:flex;align-items:center;gap:10px;font-size:17px;color:#444;white-space:nowrap}
.callbar .ring{width:42px;height:42px;border:2px solid var(--olive);border-radius:50%;display:flex;align-items:center;justify-content:center}
.callbar b{font-size:24px;color:var(--purple)}
.nav{position:absolute;left:494px;top:68px;display:flex;gap:31px;font-size:18px;color:#333;white-space:nowrap}
.nav .active{position:relative}
.nav .active::after{content:"";position:absolute;left:0;right:0;bottom:-12px;height:2px;background:var(--olive)}
/* hero */
.hero{position:absolute;left:0;top:104px;width:1200px;height:700px;background:linear-gradient(110deg,#4d4a44 0%,#8f8a80 35%,#c8c2b8 55%,#9b948c 80%,#6b6660 100%)}
.hero h1{position:absolute;left:175px;top:152px;font-size:66px;line-height:72px;font-weight:900;color:var(--white);letter-spacing:-1px}
.hero p{position:absolute;left:175px;top:324px;font-size:21px;font-weight:700;color:var(--white)}
.arrow{position:absolute;width:30px;height:30px;border-radius:50%;background:#222;display:flex;align-items:center;justify-content:center}
.dots{position:absolute;left:564px;top:564px;display:flex;gap:6px}
.dots span{width:9px;height:9px;border-radius:50%;background:var(--white)}
.dots .on{background:var(--olive)}
/* section headings */
.h2{position:absolute;font-size:42px;font-weight:900;color:var(--purple);letter-spacing:-.5px}
.copy{position:absolute;font-size:14px;line-height:29.5px;color:#555}
.photo-circle{position:absolute;border-radius:50%}
/* welcome */
.welcome{position:absolute;left:0;top:1342px;width:1200px;height:396px;background:linear-gradient(90deg,#eeeeef,#f5f4f5 50%,#ebeaec)}
/* cards */
.cards{position:absolute;left:0;top:1738px;width:1200px;height:398px;display:flex}
.card{width:300px;height:398px;border-right:1px solid var(--line);box-shadow:0 2px 4px rgba(0,0,0,.06);text-align:center;position:relative}
.card .img{position:absolute;left:7px;top:8px;width:286px;height:202px}
.card h3{position:absolute;left:0;right:0;top:245px;font-size:20px;font-weight:700;color:#222}
.card p{position:absolute;left:0;right:0;top:284px;font-size:14px;color:#666}
/* services */
.services{position:absolute;left:0;top:2745px;width:1200px;height:217px;display:flex}
.svc{width:300px;height:217px;text-align:center;color:var(--white);position:relative}
.svc.p{background:var(--purple)}
.svc.o{background:var(--olive)}
.svc .ico{position:absolute;left:120px;top:26px;width:60px;height:64px}
.svc.p .ico{color:var(--olive)}
.svc.o .ico{color:var(--white)}
.svc h4{position:absolute;left:0;right:0;font-size:16px;font-weight:700}
.svc p{position:absolute;left:30px;right:30px;font-size:10.5px;line-height:15.5px}
/* partners */
.partner{position:absolute;top:3170px;width:165px;height:81px;background:var(--white);box-shadow:0 1px 5px rgba(0,0,0,.15);display:flex;align-items:center;justify-content:center;font-size:22px;font-weight:900;color:var(--purple)}
.ring-arrow{position:absolute;top:3192px;width:38px;height:38px;border-radius:50%;border:1px solid #999;display:flex;align-items:center;justify-content:center;background:var(--white)}
/* footer */
.foot{color:var(--white)}
.hours{position:absolute;left:693px;top:3459px;width:362px;height:363px;background:var(--purple-deep)}
.hours h5{position:absolute;left:37px;top:70px;font-size:24px;font-weight:700;color:var(--olive)}
.hours .row{position:absolute;left:37px;font-size:12px;color:var(--white);display:flex;white-space:nowrap}
.hours .row span:nth-child(1){width:120px}
.hours .row span:nth-child(2){width:82px}
</style>
</head>
<body>

<header class="header">
  <div class="brand"><div class="mark"></div><div class="name">Tallowmere Chiropractic<small>WHOLISTIC HEALTH CLINIC</small></div></div>
  <div class="callbar">
    <div class="ring"><svg width="20" height="20" viewBox="0 0 24 24"><path d="M6.6 10.8a15 15 0 0 0 6.6 6.6l2.2-2.2c.3-.3.7-.4 1-.2 1.1.4 2.3.6 3.6.6.6 0 1 .4 1 1V20c0 .6-.4 1-1 1A17 17 0 0 1 3 4c0-.6.4-1 1-1h3.5c.6 0 1 .4 1 1 0 1.3.2 2.5.6 3.6.1.3 0 .7-.2 1z" fill="#bcb383"/></svg></div>
    Call Us Today : <b>(02) 9000 4417</b>
  </div>
  <div class="btn" style="left:835px;top:8px;width:220px;height:40px;font-size:11px">Make an appointment <span class="dot"></span></div>
  <nav class="nav"><span class="active">Home</span><span>About Us</span><span>Team</span><span>Contact</span><span>Terms of service</span><span>Privacy</span></nav>
</header>

<section class="hero" role="img" aria-label="Photo of a chiropractor adjusting a patient's lower back in a clinic">
  <h1>TALLOWMERE<br>CHIROPRACTIC</h1>
  <p>Lorem ipsum dolor sit amet consectetur adipiscing elit</p>
  <div class="btn" style="left:178px;top:397px;width:188px;height:60px;font-size:18px;font-weight:700">GET STARTED <span class="dot"></span></div>
  <div class="arrow" style="left:84px;top:313px"><svg width="10" height="12" viewBox="0 0 10 12"><path d="M7 1 2 6l5 5" stroke="#fff" stroke-width="2" fill="none"/></svg></div>
  <div class="arrow" style="left:1085px;top:313px"><svg width="10" height="12" viewBox="0 0 10 12"><path d="M3 1l5 5-5 5" stroke="#fff" stroke-width="2" fill="none"/></svg></div>
  <div class="dots"><span></span><span></span><span class="on"></span><span></span><span></span></div>
</section>
<svg class="abs" style="left:0;top:680px" width="1200" height="130" viewBox="0 0 1200 130">
  <path d="M0 60 C250 0 450 10 650 60 C850 110 1050 90 1200 60 L1200 130 L0 130Z" fill="#fff"/>
  <path d="M0 98 C200 30 420 40 620 90 C820 130 1000 110 1200 70 L1200 80 C1000 118 820 140 620 104 C420 60 220 50 0 108Z" fill="#bcb383"/>
  <path d="M0 75 C220 20 430 25 630 78 C830 120 1030 100 1200 50 L1200 62 C1030 110 830 128 630 92 C430 45 220 40 0 90Z" fill="#3f3650"/>
</svg>

<!-- Who we are -->
<svg class="abs" style="left:130px;top:858px" width="440" height="434" viewBox="0 0 440 434"><path d="M220 10 A212 212 0 0 0 220 424" stroke="#bcb383" stroke-width="3" fill="none"/></svg>
<div class="photo-circle" style="left:140px;top:862px;width:425px;height:425px;background:linear-gradient(135deg,#e9e7e2,#c9b89a 45%,#2f6f5e 75%,#e4e2dd)" role="img" aria-label="Photo of a practitioner treating the shoulder of a woman lying face down"></div>
<h2 class="h2" style="left:611px;top:882px">WHO WE ARE</h2>
<p class="copy" style="left:612px;top:963px;width:445px">Tallowmere Chiropractic, situated in Kirrawee Heights and established for 40 years, is passionate about helping you achieve your vitality and regain your health.&nbsp; We use a unique wholistic approach, understand you are an individual and tailor your treatment accordingly.</p>
<p class="copy" style="left:612px;top:1111px;width:460px">We understand your health may be affected by structural, biochemical or emotional factors and address these issues in your tailored care plan.</p>
<div class="btn" style="left:612px;top:1204px;width:162px;height:51px;font-size:15px">READ MORE <span class="dot"></span></div>

<!-- Welcome -->
<section class="welcome" role="img" aria-label="Faded background photo of a treatment session">
  <svg class="abs" style="left:0;top:0" width="1200" height="60" viewBox="0 0 1200 60"><path d="M0 0 H1200 V0 C1000 -10 800 5 620 40 C420 80 200 60 0 50Z" fill="#fff"/></svg>
  <h2 class="h2" style="left:0;right:0;top:176px;text-align:center">WELCOME TO</h2>
  <p class="abs" style="left:0;right:0;top:250px;text-align:center;font-size:28px;line-height:39px;color:#333">The nations leading Wholistic Health<br>and Wellness Centre</p>
</section>

<section class="cards">
  <div class="card"><div class="img" role="img" aria-label="Photo of smiling children" style="background:linear-gradient(135deg,#8ab5dd,#d9a985 55%,#a43a3a)"></div><h3>Happy Balanced Kids</h3><p>For the best start in life</p><div class="btn" style="left:87px;top:327px;width:126px;height:37px;font-size:11px">Read more <span class="dot"></span></div></div>
  <div class="card"><div class="img" role="img" aria-label="Photo of a fit woman in sportswear" style="background:linear-gradient(135deg,#b8c3cb,#a7b2ba 50%,#3a4c55)"></div><h3>Healthy Bodies</h3><p>We focus on establishing the best</p><div class="btn" style="left:87px;top:327px;width:126px;height:37px;font-size:11px">Read more <span class="dot"></span></div></div>
  <div class="card"><div class="img" role="img" aria-label="Photo of a man's back with highlighted spine" style="background:linear-gradient(135deg,#5a4a42,#a36e55 50%,#c04a40)"></div><h3>Improved Performance</h3><p>To achieve your personal best</p><div class="btn" style="left:87px;top:327px;width:126px;height:37px;font-size:11px">Read more <span class="dot"></span></div></div>
  <div class="card"><div class="img" role="img" aria-label="Photo of a man exercising on a mat at home" style="background:linear-gradient(135deg,#dcd9d4,#bdb8b0 50%,#3d78b8)"></div><h3>You</h3><p>To be the best you can be</p><div class="btn" style="left:87px;top:327px;width:126px;height:37px;font-size:11px">Read more <span class="dot"></span></div></div>
</section>

<!-- What we do -->
<h2 class="h2" style="left:145px;top:2248px">WHAT WE DO</h2>
<p class="copy" style="left:145px;top:2330px;width:440px">Our clinics Chiropractic procedures are extremely safe and gentle and can be applied to all phases of life for optimum health, from the newborn to the elderly. Your tailored care may include a combination of Chiropractic, Osteopathy, Nutrition, Acupuncture, Applied Kinesiology, Exercise Prescription, Decompression Therapy, Massage, VEGA testing and Stress Management Techniques to get to the cause of your health concerns.</p>
<div class="btn" style="left:145px;top:2573px;width:162px;height:50px;font-size:15px">READ MORE <span class="dot"></span></div>
<svg class="abs" style="left:630px;top:2225px" width="430" height="430" viewBox="0 0 430 430"><path d="M215 5 A210 210 0 0 1 215 425" stroke="#bcb383" stroke-width="3" fill="none"/></svg>
<div class="photo-circle" style="left:625px;top:2232px;width:420px;height:420px;background:linear-gradient(135deg,#eeeceb,#d7b9a6 45%,#6f9cc9 80%,#e8e6e4)" role="img" aria-label="Photo of a practitioner examining a woman's spine"></div>

<section class="services">
  <div class="svc p">
    <svg class="ico" viewBox="0 0 60 64" fill="none" stroke="currentColor" stroke-width="2.5" stroke-linecap="round"><rect x="22" y="4" width="16" height="10" rx="3"/><rect x="20" y="19" width="20" height="10" rx="3"/><rect x="20" y="34" width="20" height="10" rx="3"/><rect x="22" y="49" width="16" height="10" rx="3"/><path d="M12 24h6M42 24h6M12 39h6M42 39h6"/></svg>
    <h4 style="top:120px">CHIROPRACTIC</h4><p style="top:151px">Lorem ipsum dolor sit consectetur adipiscing elit, sed do eiusmod tempor incididuntut labore et dolore magna aliqua</p></div>
  <div class="svc o">
    <svg class="ico" viewBox="0 0 60 64" fill="none" stroke="currentColor" stroke-width="2.5" stroke-linecap="round"><rect x="14" y="6" width="34" height="52" rx="4"/><path d="M22 18h18M22 28h18M22 38h18M22 48h10"/></svg>
    <h4 style="top:114px">OSTEOPATHY</h4><p style="top:151px">Lorem ipsum dolor sit consectetur adipiscing elit, sed do eiusmod tempor incididuntut labore et dolore magna aliqua</p></div>
  <div class="svc p">
    <svg class="ico" viewBox="0 0 60 64" fill="none" stroke="currentColor" stroke-width="2.5" stroke-linecap="round"><path d="M18 8h16M20 8v10l-8 10v28h28V28l-8-10V8"/><path d="M12 38h28"/><circle cx="48" cy="46" r="6"/></svg>
    <h4 style="top:120px">DETOXIFICATION</h4><p style="top:151px">Lorem ipsum dolor sit consectetur adipiscing elit, sed do eiusmod tempor incididuntut labore et dolore magna aliqua</p></div>
  <div class="svc o">
    <svg class="ico" viewBox="0 0 60 64" fill="none" stroke="currentColor" stroke-width="2.5" stroke-linecap="round"><rect x="10" y="8" width="40" height="48" rx="4"/><circle cx="30" cy="30" r="10"/><path d="M30 24v12M24 30h12M18 48h24"/></svg>
    <h4 style="top:114px">DIGESTION</h4><p style="top:151px">Lorem ipsum dolor sit consectetur adipiscing elit, sed do eiusmod tempor incididuntut labore et dolore magna aliqua</p></div>
</section>
<div class="abs" style="left:0;top:2828px;width:22px;height:54px;background:var(--purple);border:1px solid #fff;display:flex;align-items:center;justify-content:center"><svg width="8" height="12"><path d="M6 1 1 6l5 5" stroke="#fff" stroke-width="1.5" fill="none"/></svg></div>
<div class="abs" style="left:1178px;top:2828px;width:22px;height:54px;background:var(--olive);border:1px solid #fff;display:flex;align-items:center;justify-content:center"><svg width="8" height="12"><path d="M2 1l5 5-5 5" stroke="#fff" stroke-width="1.5" fill="none"/></svg></div>

<!-- Partners -->
<h2 class="h2" style="left:0;right:0;top:3062px;text-align:center">OUR PARTNERS</h2>
<div class="ring-arrow" style="left:79px"><svg width="8" height="12"><path d="M6 1 1 6l5 5" stroke="#333" stroke-width="1.5" fill="none"/></svg></div>
<div class="partner" style="left:144px">NRB</div>
<div class="partner" style="left:331px">PLUVEX</div>
<div class="partner" style="left:518px">VITALOAN</div>
<div class="partner" style="left:705px">JOBSHIELD</div>
<div class="partner" style="left:892px">RTQ</div>
<div class="ring-arrow" style="left:1082px"><svg width="8" height="12"><path d="M2 1l5 5-5 5" stroke="#333" stroke-width="1.5" fill="none"/></svg></div>

<!-- Footer -->
<svg class="abs" style="left:0;top:3345px" width="1200" height="477" viewBox="0 0 1200 477" preserveAspectRatio="none">
  <path d="M0 95 C250 20 500 10 700 40 C900 70 1050 40 1200 10 L1200 477 L0 477Z" fill="#3f3650"/>
  <path d="M0 78 C250 5 500 -5 700 25 C900 55 1050 25 1200 0 L1200 10 C1050 40 900 70 700 40 C500 10 250 20 0 95Z" fill="#bcb383"/>
</svg>
<footer class="foot">
  <div class="abs" style="left:145px;top:3455px;display:flex;align-items:center;gap:9px"><div style="width:36px;height:36px;border-radius:50%;background:var(--white)"></div><div style="font-size:14px;line-height:1.1">Tallowmere Chiropractic<br><span style="font-size:8px">WHOLISTIC HEALTH CLINIC</span></div></div>
  <p class="abs" style="left:145px;top:3520px;font-size:11px;line-height:18px">27 Wattlebrook Rd<br>KIRRAWEE HEIGHTS NSW 2232</p>
  <p class="abs" style="left:145px;top:3578px;font-size:11px;display:flex;gap:10px;align-items:center"><svg width="16" height="16" viewBox="0 0 24 24"><path d="M6.6 10.8a15 15 0 0 0 6.6 6.6l2.2-2.2c.3-.3.7-.4 1-.2 1.1.4 2.3.6 3.6.6.6 0 1 .4 1 1V20c0 .6-.4 1-1 1A17 17 0 0 1 3 4c0-.6.4-1 1-1h3.5c.6 0 1 .4 1 1 0 1.3.2 2.5.6 3.6.1.3 0 .7-.2 1z" stroke="#fff" fill="none" stroke-width="1.5"/></svg>Phone: (02) 9000 4417</p>
  <p class="abs" style="left:145px;top:3612px;font-size:11px;display:flex;gap:10px;align-items:center"><svg width="16" height="12" viewBox="0 0 16 12"><rect x=".5" y=".5" width="15" height="11" stroke="#fff" fill="none"/><path d="M.5.5 8 7l7.5-6.5" stroke="#fff" fill="none"/></svg>contact@tallowmerechiro.com.au</p>
  <p class="abs" style="left:144px;top:3680px;font-size:14px;font-weight:700;white-space:nowrap">HOME&nbsp; / &nbsp;ABOUT US&nbsp; / &nbsp;TEAM&nbsp; / &nbsp;CONTACT&nbsp; / &nbsp;TERMS OF SERVICE&nbsp; / &nbsp;PRIVACY</p>
  <p class="abs" style="left:144px;top:3721px;font-size:10px">2020 © Copyrights Tallowmere Chiropractic . All Rights Reserved</p>
  <div class="abs" style="left:144px;top:3759px;display:flex;gap:5px">
    <span style="width:22px;height:22px;border:1px solid #fff;border-radius:50%"></span><span style="width:22px;height:22px;border:1px solid #fff;border-radius:50%"></span><span style="width:22px;height:22px;border:1px solid #fff;border-radius:50%"></span><span style="width:22px;height:22px;border:1px solid #fff;border-radius:50%"></span>
  </div>
  <h5 class="abs" style="left:426px;top:3502px;font-size:18px;font-weight:700">STAY IN CONTACT</h5>
  <div class="abs" style="left:426px;top:3547px;width:212px;height:37px;background:var(--white);color:#777;font-size:10px;padding:11px 12px">Enter email</div>
  <div class="abs" style="left:426px;top:3598px;width:96px;height:38px;background:var(--olive);font-size:11px;display:flex;align-items:center;justify-content:center">SUBSCRIBE</div>
  <div class="hours">
    <h5>CLINIC HOURS</h5>
    <div class="row" style="top:136px"><span>MONDAY</span><span>9 - 12 AM</span><span>1:30 - 6:30 PM</span></div>
    <div class="row" style="top:167px"><span>TUESDAY</span><span>2.30 - 6.30 PM</span></div>
    <div class="row" style="top:198px"><span>WEDNESDAY</span><span>&nbsp;8 AM - 7 PM</span></div>
    <div class="row" style="top:229px"><span>THURSDAY</span><span>&nbsp;2.30 - 6.30 PM</span></div>
    <div class="row" style="top:260px"><span>FRIDAY</span><span>9 - 12 AM</span><span>1:30 - 6:30 PM</span></div>
    <div class="row" style="top:291px"><span>SATURDAY</span><span>8 AM - 1 PM</span></div>
  </div>
</footer>
</body>
</html>
```